Personal Chef Needs a Good Web Design

Hi everyone!
My name is Lev, I work as a private chef for last 10 years, traveling all around the world and cooking in private megayacht and villas.
I'm about to settle down in my hometown in Europe for a while. And therefore I need a website that will show my story, pics and recipes, nutritional advices and of course offer a Personal and Private Chef services( working for 4-5 families and bringing delicious food to their house).
My clients are extremely rich folks, but usually are down to earth ones.
I believe, the web site should be focused on attention to:
-VIP person's wife( as she is usually responsible for food for family) and be simple.
-to famous people agents and be on high level.

There will be about 10 different menus and 6 different service offers

--UPDATE--
Logo Design:
+My thoughts are- printed structure of the vegetable or fruit on a white font. Like you slice the buffalo tomato, put it in red paint and print it on the edge of the page. See attached files named logo. Can be any nice structured thing, like tomato, lemon, red cabbage etc.
+Classic logos with chef's hat or knives are good too.
+Need to have the space for me to add the name( the fonts can be provided)

Target Market(s)

Private person. 80% Russian clients.

Industry/Entity Type

Cooking

Coding

Coded - Design and coding required

Number of Pages Required

3 page

Requirements
Must have
• Contact form/ Request back call/ Schedule a free consultation
Nice to have
• The client will need to choose straight ahead from the range of services I offer, like:
• -Private Chef( cooking only for the client)
• -Personal Chef( cooking for around 5 clients, bringing the ready to be heated food to their door)
• -Romantic dinner for two
• -Professional Sommelier service
• -Build your kitchen( offering design, equipment and that will fit your requirements)
• -Other( flowers, waiters, barista, equipment rental)
• So this column should go right after the introduction/aboutme part and will lead to separate pages with how-it-works thing for each.

```html
<!DOCTYPE html>
<html lang="en">
<head>
<meta charset="utf-8">
<title>Lev Personal Chef – New Recipes</title>
<link href="https://fonts.googleapis.com/css2?family=Lato:wght@400;700&family=Montserrat:wght@800&display=swap" rel="stylesheet">
<style>
:root{
  --gold:#c6a24a;
  --gold-dark:#b8923a;
  --ink:#1d1d1d;
  --text:#3a3a3a;
  --muted:#6b6b6b;
  --panel:#f4f4f4;
  --line:#d9d9d9;
  --black:#0c0c0c;
  --white:#ffffff;
  --orange:#d9643a;
  --grey-btn:#8e8e8e;
}
*{box-sizing:border-box;margin:0;padding:0}
html,body{width:762px;height:1200px;overflow:hidden;background:var(--white)}
body{position:relative;font-family:"Lato",Arial,sans-serif;color:var(--text)}
.abs{position:absolute}

/* hero */
.hero{left:0;top:0;width:762px;height:294px;
  background:radial-gradient(ellipse at 30% 60%,#6a4a34 0%,#3a2a22 45%,#1e1714 100%);}
.hero-shade{left:0;top:0;width:762px;height:294px;background:linear-gradient(#0008,#0004 40%,#0006)}
.brand{left:62px;top:14px;display:flex;align-items:center;gap:8px}
.brand-mark{width:48px;height:48px;border-radius:50%;background:var(--gold);border:3px solid var(--white)}
.brand-name{color:var(--white);font-size:13px;font-weight:400;line-height:1.25;letter-spacing:.5px}
.brand-name b{font-weight:400;font-size:19px;letter-spacing:1px;display:block}
.nav{top:33px;left:384px;display:flex;gap:0}
.nav a{color:var(--white);text-decoration:none;font-size:12px;position:absolute;white-space:nowrap}
.nav a.active{color:var(--gold)}
.nav a.active::after{content:"";position:absolute;left:0;right:0;bottom:-6px;height:2px;background:var(--gold)}
.hero-title{left:0;width:762px;top:116px;text-align:center;color:var(--white);font-family:"Montserrat",Arial,sans-serif;font-weight:800;font-size:40px;letter-spacing:1px}
.hero-sub{left:0;width:762px;top:168px;text-align:center;color:var(--white);font-size:20px;display:flex;justify-content:center;align-items:center;gap:14px}
.dot{width:9px;height:9px;border:1.5px solid var(--white);border-radius:50%;position:relative}
.dot::after{content:"";position:absolute;left:2px;top:2px;width:2px;height:2px;background:var(--white);border-radius:50%}
.hero-btn{left:332px;top:206px;width:98px;height:40px;border:2px solid var(--white);padding:3px}
.hero-btn span{display:flex;width:100%;height:100%;background:var(--gold);color:var(--white);font-size:14px;align-items:center;justify-content:center}

/* section heading */
.section-title{left:0;width:762px;top:321px;text-align:center;font-size:27px;color:var(--ink)}
.section-title em{font-style:normal;color:var(--gold)}
.divider{left:217px;top:368px;width:329px;height:8px}

/* sidebar */
.types{left:63px;top:409px;width:158px;height:147px;background:var(--panel);border-bottom:1px solid var(--line)}
.types h3{position:absolute;left:19px;top:14px;font-size:11px;font-weight:400;color:var(--ink)}
.types hr{position:absolute;left:19px;top:33px;width:126px;border:0;border-top:1px solid var(--line)}
.types ul{list-style:none;position:absolute;left:16px;top:45px}
.types li{font-size:10px;color:var(--ink);height:23.5px;display:flex;gap:10px}
.types li::before{content:"›";color:var(--muted)}
.types li.current{color:var(--gold)}

/* recipe */
.recipe-title{left:238px;top:408px;font-size:23px;color:var(--gold)}
.recipe-photo{left:238px;top:458px;width:462px;height:189px;
  background:linear-gradient(100deg,#6b3a1c 0%,#c4542a 35%,#d8743e 55%,#d9c07a 75%,#b9c25a 90%,#e6dca0 100%)}
.facts{left:238px;top:647px;width:462px;height:44px;background:#f7f7f7}
.fact{position:absolute;top:7px;font-size:9.5px;color:var(--muted)}
.fact b{display:flex;align-items:center;gap:5px;font-weight:400;color:var(--text);font-size:8.5px;margin-top:7px}
.sep{position:absolute;top:6px;width:1px;height:32px;background:var(--line)}
.btn{position:absolute;top:8px;height:18px;color:var(--white);font-size:8px;display:flex;align-items:center;justify-content:center;gap:4px}
.btn.fav{left:328px;width:65px;background:var(--orange)}
.btn.mail{left:397px;width:57px;background:var(--grey-btn)}

.sub-title{font-size:13.5px;color:var(--gold)}
.desc{left:64px;top:748px;width:626px;font-size:8.2px;line-height:15.6px;color:var(--ink)}

.ingredients{left:63px;top:862px;width:207px;height:154px;background:var(--panel);border-top:1px solid var(--gold)}
.ingredients ul{list-style:none;position:absolute;left:13px;top:16px}
.ingredients li{font-size:8.2px;color:var(--ink);height:21.2px;display:flex;gap:8px}
.ingredients li::before{content:"";width:7px;height:7px;border:1px solid #ccc;background:var(--white);margin-top:1px}

.steps{left:303px;top:864px;width:390px;list-style:none}
.step{position:absolute;left:0;display:flex;gap:15px;font-size:9.5px;line-height:13.6px;color:var(--ink)}
.step i{font-style:normal;width:18px;height:18px;background:var(--panel);font-size:8px;color:var(--muted);display:flex;align-items:center;justify-content:center;flex:none}

/* footer */
.footer{left:0;top:1074px;width:762px;height:98px;background:var(--black)}
.foot-nav{left:66px;top:1091px;font-size:10px;color:var(--white)}
.foot-nav span{position:absolute;white-space:nowrap}
.foot-rule{left:63px;top:1114px;width:503px;height:1px;background:#2a2a2a}
.contact{position:absolute;top:1128px;display:flex;gap:8px;color:var(--white)}
.contact .ic{width:22px;height:22px;border:1.5px solid var(--white);border-radius:50%;display:flex;align-items:center;justify-content:center;flex:none}
.contact b{font-size:8.5px;display:block}
.contact small{font-size:7.3px;display:block;margin-top:3px}
.foot-brand{left:584px;top:1109px;display:flex;align-items:center;gap:8px}
.foot-brand .brand-mark{width:38px;height:38px;border-width:2px}
.foot-brand .brand-name{font-size:10.5px;letter-spacing:1.5px}
.foot-brand .brand-name b{font-size:17px}
.bar{left:0;top:1172px;width:762px;height:28px;background:var(--gold)}
.copy{left:64px;top:1181px;font-size:7.5px;color:var(--ink)}
.social{position:absolute;top:1175px;width:21px;height:21px;border:1.5px solid var(--ink);border-radius:50%}
</style>
</head>
<body>

<header>
  <div class="abs hero" role="img" aria-label="Seafood platter with mussels, prawns and lemon"></div>
  <div class="abs hero-shade"></div>
  <div class="abs brand">
    <div class="brand-mark"></div>
    <div class="brand-name"><b>LEV</b>PERSONAL CHEF</div>
  </div>
  <nav class="abs nav">
    <a style="left:0">Home</a>
    <a style="left:63px">Services</a>
    <a style="left:134px">Gallery</a>
    <a class="active" style="left:204px">Menu</a>
    <a style="left:263px">Contact Us</a>
  </nav>
  <h1 class="abs hero-title">I AM SPECIALIST IN</h1>
  <div class="abs hero-sub"><span>Seafood</span><i class="dot"></i><span>Chicken</span><i class="dot"></i><span>Beef</span><i class="dot"></i><span>Pork</span></div>
  <div class="abs hero-btn"><span>Contact Us</span></div>
</header>

<main>
  <h2 class="abs section-title"><em>New</em> Recipes</h2>
  <svg class="abs divider" viewBox="0 0 329 8"><line x1="0" y1="4" x2="159" y2="4" stroke="#c8c8c8"/><line x1="170" y1="4" x2="329" y2="4" stroke="#c8c8c8"/><circle cx="164.5" cy="4" r="3.3" fill="none" stroke="#999"/><circle cx="164.5" cy="4" r="1.1" fill="#999"/></svg>

  <aside class="abs types">
    <h3>RECIPE TYPES</h3>
    <hr>
    <ul>
      <li class="current">Seafood</li>
      <li>Chicken</li>
      <li>Beef</li>
      <li>Pork</li>
    </ul>
  </aside>

  <h2 class="abs recipe-title">Seafood</h2>
  <div class="abs recipe-photo" role="img" aria-label="Grilled prawns with rice and a lime half"></div>
  <div class="abs facts">
    <div class="fact" style="left:11px">Prep Time<b><svg width="10" height="10" viewBox="0 0 10 10"><circle cx="5" cy="5" r="4.3" fill="none" stroke="#333"/><path d="M5 2.5V5h2" fill="none" stroke="#333"/></svg>10 minutes</b></div>
    <div class="sep" style="left:86px"></div>
    <div class="fact" style="left:100px">Cook Time<b><svg width="10" height="10" viewBox="0 0 10 10"><circle cx="5" cy="5" r="4.3" fill="none" stroke="#333"/><path d="M5 2.5V5h2" fill="none" stroke="#333"/></svg>15 minutes</b></div>
    <div class="sep" style="left:175px"></div>
    <div class="fact" style="left:189px">Serving<b>For 4 People</b></div>
    <div class="sep" style="left:261px"></div>
    <div class="fact" style="left:271px">Difficulty<b>Medium</b></div>
    <div class="btn fav"><svg width="8" height="8" viewBox="0 0 10 9"><path d="M5 9L1 5a2.3 2.3 0 0 1 4-3a2.3 2.3 0 0 1 4 3z" fill="#fff"/></svg>FAVORITE</div>
    <div class="btn mail"><svg width="10" height="8" viewBox="0 0 10 8"><rect x=".5" y=".5" width="9" height="7" fill="none" stroke="#fff"/><path d="M.5 .5L5 4.5L9.5 .5" fill="none" stroke="#fff"/></svg>E-MAIL</div>
  </div>

  <h3 class="abs sub-title" style="left:64px;top:720px">Recipe Description</h3>
  <p class="abs desc">Lorem ipsum dolor sit amet, consectetuer adipiscing elit, sed diam nonummy nibh euismod tincidunt ut laoreet dolore magna aliquam erat volutpat. Ut wisi enim ad minim veniam, quis nostrud exerci tation ullamcorper suscipit lobortis nisl ut aliquip ex ea commodo consequat. Duis autem vel eum iriure dolor in hendrerit in vulputate velit esse molestie consequat, vel illum dolore eu feugiat nulla facilisis at vero eros et accumsan et iusto odio dignissim qui blandit praesent luptatum zzril delenit augue duis dolore te feugait nulla facilisis.</p>

  <h3 class="abs sub-title" style="left:64px;top:830px">Recipe Ingredient</h3>
  <div class="abs ingredients">
    <ul>
      <li>300g (10oz) cauliflower, cut into florets</li>
      <li>1 tbsp vegetable oil</li>
      <li>1 garlic clove, finely chopped</li>
      <li>1 red chilli, deseeded and finely chopped</li>
      <li>1 courgette, cut into ribbons</li>
      <li>50g (2oz) frozen garden peas, defrosted</li>
    </ul>
  </div>

  <h3 class="abs sub-title" style="left:304px;top:830px">Instructions</h3>
  <ol class="abs steps">
    <li class="step" style="top:0"><i>1</i><span>Preheat oven to 180°C/160°C fan-forced. Crush 1 garlic clove. Thinly slice<br>remaining garlic.</span></li>
    <li class="step" style="top:39px"><i>2</i><span>Heat half the oil in a large, flameproof casserole dish over medium heat.<br>Add the onion.</span></li>
    <li class="step" style="top:78px"><i>3</i><span>Cook, stirring, for 5 minutes or until softened. Add the crushed garlic. Cook,<br>stirring, for 1 minute.</span></li>
    <li class="step" style="top:117px"><i>4</i><span style="padding-top:2px">Add rice. Stir to coat. Add stock and chilli.</span></li>
    <li class="step" style="top:149px"><i>5</i><span>Bring to the boil. Cover with foil. Transfer to oven. Bake for 10 minutes or until<br>half the liquid has been absorbed.</span></li>
  </ol>
</main>

<footer>
  <div class="abs footer"></div>
  <div class="abs foot-nav">
    <span style="left:0">HOME</span><span style="left:52px">|</span>
    <span style="left:77px">Services</span><span style="left:137px">|</span>
    <span style="left:161px">Gallery</span><span style="left:215px">|</span>
    <span style="left:240px">Menu</span><span style="left:287px">|</span>
    <span style="left:312px">Contact Us</span>
  </div>
  <div class="abs foot-rule"></div>
  <div class="contact" style="left:65px">
    <span class="ic"><svg width="10" height="12" viewBox="0 0 10 12"><path d="M5 11.5C2 7.5 1 6 1 4.2a4 4 0 0 1 8 0C9 6 8 7.5 5 11.5z" fill="none" stroke="#fff"/><circle cx="5" cy="4.3" r="1.4" fill="#fff"/></svg></span>
    <div><b>Lev Pesonal Chef</b><small>48, Vellum Lane, Orrin Park - 204518</small></div>
  </div>
  <div class="contact" style="left:287px">
    <span class="ic"><svg width="11" height="11" viewBox="0 0 11 11"><path d="M2 1l2 2-1 1.5c.7 1.5 2 2.8 3.5 3.5L8 7l2 2-1.5 1.5C4.5 10 1 6.5.5 2.5z" fill="#fff"/></svg></span>
    <div><b>Call Us :</b><small style="font-size:8.5px">012-555-0147</small></div>
  </div>
  <div class="contact" style="left:416px">
    <span class="ic"><svg width="10" height="8" viewBox="0 0 10 8"><rect x=".5" y=".5" width="9" height="7" fill="#fff"/><path d="M.5 .5L5 4.5L9.5 .5" fill="none" stroke="#000"/></svg></span>
    <div><b>Email Us :</b><small>info@levpersonalchef.com</small></div>
  </div>
  <div class="abs foot-brand">
    <div class="brand-mark"></div>
    <div class="brand-name"><b>LEV</b>PERSONAL CHEF</div>
  </div>
  <div class="abs bar"></div>
  <p class="abs copy">Copyright © 2016 HARBOUR TABLE CO. All Rights Reserved.</p>
  <span class="social" style="left:590px"></span>
  <span class="social" style="left:617px"></span>
  <span class="social" style="left:644px"></span>
</footer>

</body>
</html>
```